Professional, polished website design for boutique wealth management firm

Hello, thank you for your interest. PLEASE READ THE BRIEF BEFORE SUBMITTING THE DESIGN.-
PLEASE USE THE ATTACHED HOME PAGE COPY FOR THIS DESIGN.
We are looking for a professional, polished design that helps portray trust and credibility for a well-established independent wealth management firm. We have copy we've written for the home page and we'd like the design and imagery to play up the copy, so there's a better chance someone will read it all. So the headlines etc should all be easy to read and the design should draw the eye towards them. For colors, again trust is important so probably blue as a dominant color, but you can also use gray, green, etc. We'd like to avoid too much use of the color red (due to financial, association with loss). SO PLEASE AVOID USE OF THE COLOR RED. We also like bright orange or yellow for call to action buttons.

Please keep the design EASY TO MAINTAIN in wordpress as well.

I have attached home page copy as well as logo files.

Here's some sites that we like so feel free to use as inspiration:
https://www.brovaltcapitalworks.example/, https://harborpathpensionsplains.example/
https://tavrin-oakes.example/, https://plantfornextyear.example/, https://ferngatefinancial.example/

As another option/idea, I like the idea of a simple format with a clean image similar to this for the home page: https://www.pixmeadowstock.example/detail/photo/calculator-falling-royalty-free-image/31684207?adppopup=true
Just an idea.

Also please be sure to incorporate the QWA /Accredited Wealth Steward logo as well, farther down the page is fine.

Thank you for your help! Feel free to contact me with any questions.

Target Market(s)

Individuals aged 48-62 who are looking to maximize their wealth, such as business owners, executives, engineers, successful tradespeople, etc.

Industry/Entity Type

Finance--wealth management

Font styles to use
Sans Serif

Requirements
Must have
• Professional and polished, Call to action buttons must be clear and stand out, headlines must be clear and stand out, also text must be big enough to be easily readable by most people
Should not have
• Anything casual, frilly, etc.

```html
<!DOCTYPE html>
<html lang="en">
<head>
<meta charset="utf-8">
<title>Meridale Asset Advisors – Wealth Management Firm</title>
<link rel="stylesheet" href="https://fonts.googleapis.com/css2?family=Merriweather:wght@400;700&family=Poppins:wght@300;400;500&display=swap">
<style>
:root{
  --navy:#1b1f4b;
  --navy-deep:#161a44;
  --royal:#2e3a96;
  --royal-soft:#5664b8;
  --ink:#141414;
  --body:#555a66;
  --orange:#f7941d;
  --pale:#eef2f9;
  --pale-blue:#dfe7f6;
  --white:#ffffff;
}
*{margin:0;padding:0;box-sizing:border-box}
html,body{width:1200px;height:3574px;overflow:hidden;background:var(--white)}
body{font-family:"Poppins",sans-serif;color:var(--body);position:relative}
.serif{font-family:"Merriweather",serif}
section,header,footer{position:absolute;left:0;width:1200px}
.abs{position:absolute}
.btn{position:absolute;display:flex;align-items:center;justify-content:center;font-family:"Merriweather",serif;font-weight:700;font-size:15px;color:var(--white);border-radius:20px;text-decoration:none}
.btn-blue{background:linear-gradient(90deg,#28338c,#5563bd)}
.btn-orange{background:var(--orange);border-radius:8px}
.heading{font-family:"Merriweather",serif;font-weight:700;font-size:28px;line-height:38px;color:var(--ink);text-align:center}
.heading .accent{color:var(--royal)}
.copy{font-size:12px;line-height:19.5px;color:var(--body)}

/* top bar + header */
.topbar{top:0;height:30px;background:var(--royal)}
.topbar .phone{left:860px;top:5px;color:var(--white);font-size:14px;display:flex;align-items:center;gap:8px}
.topbar .start{left:986px;top:0;width:154px;height:30px;background:#c7d4f0;color:var(--navy);font-family:"Merriweather",serif;font-size:12px;display:flex;align-items:center;justify-content:center}
.site-header{top:30px;height:63px;background:var(--navy)}
.brand{display:flex;align-items:center;gap:10px}
.brand .mark{width:30px;height:30px;border-radius:50%;background:var(--royal-soft)}
.brand .name{font-family:"Merriweather",serif;font-weight:700;color:var(--white);font-size:21px;line-height:1}
.site-header .brand{left:64px;top:17px}
.nav{left:620px;top:24px;display:flex;gap:0}
.nav a{color:#e6e9f5;font-size:11.5px;text-decoration:none;position:absolute;white-space:nowrap}
.nav .caret{position:absolute;left:17px;top:18px;width:0;height:0;border-left:4px solid transparent;border-right:4px solid transparent;border-top:5px solid var(--white)}
.badge{left:1004px;top:13px;width:136px;height:36px;display:flex;gap:6px;align-items:center}
.badge .box{width:60px;height:34px;border:2px solid var(--white);border-radius:3px}
.badge .lines{display:flex;flex-direction:column;gap:5px}
.badge .lines span{display:block;width:64px;height:3px;background:var(--white)}

/* hero */
.hero{top:93px;height:614px;background:linear-gradient(90deg,#f3f4f7 0%,#e9eaef 40%,#cfd3dc 100%)}
.hero-photo{left:430px;top:0;width:770px;height:614px;background:linear-gradient(120deg,#e7e9ee 0%,#b9bfcb 45%,#4b5d8e 80%,#2f3f70 100%)}
.hero-wave{left:0;top:0}
.hero h1{left:61px;top:106px;font-family:"Merriweather",serif;font-weight:700;font-size:39px;line-height:49px;color:var(--ink)}
.hero h1 .accent{color:var(--royal)}
.hero .tag{left:61px;top:258px;font-size:17px;color:#7d86c9}
.hero .btn{left:61px;top:290px;width:180px;height:38px}

/* tax planning */
.tax{top:707px;height:369px}
.tax .heading{top:94px;width:1200px}
.tax .copy{left:320px;top:180px;width:560px;text-align:center}
.tax .btn{left:476px;top:254px;width:247px;height:39px}

/* strategies */
.strategies{top:1076px;height:697px;background:var(--pale)}
.strategies .heading{top:75px;width:1200px}
.strategies .sub{top:164px;width:1200px;text-align:center;font-size:13.5px;color:#444}
.card-photo{top:221px;width:345px;height:232px}
.card-photo.p1{left:60px;background:linear-gradient(135deg,#1c1c1e,#4a4a4c 55%,#2b2b2d)}
.card-photo.p2{left:427px;background:linear-gradient(135deg,#6cb7c8,#3a8ea5 60%,#2f7b92)}
.card-photo.p3{left:795px;background:linear-gradient(135deg,#b7c5dd,#eef1f7 50%,#9fb2d4)}
.card{top:405px;width:300px;height:218px;background:var(--white);border-bottom:4px solid var(--royal);text-align:center;padding:28px 22px 0}
.card.c1{left:83px}.card.c2{left:450px}.card.c3{left:818px}
.card h3{font-family:"Merriweather",serif;font-weight:700;font-size:17px;color:var(--ink);margin-bottom:14px}
.card p{font-size:11px;line-height:19.5px;color:#666;height:78px;overflow:hidden}
.card a{display:inline-block;margin-top:19px;font-family:"Merriweather",serif;font-size:13px;color:#7d86c9;text-decoration:underline}

/* difference */
.difference{top:1773px;height:524px}
.difference h2{left:153px;top:100px;font-family:"Merriweather",serif;font-weight:700;font-size:28px;line-height:37.5px;color:var(--ink)}
.difference h2 .accent{color:var(--royal)}
.difference .copy{left:153px;top:305px;width:410px;font-size:11.5px}
.difference .btn{left:153px;top:400px;width:202px;height:39px}
.diff-art{left:721px;top:0;width:479px;height:524px;background:linear-gradient(90deg,#9aa6d8 0%,#3c49a4 40%,#1f2b8f 100%);border-radius:60px 0 0 60px}
.diff-ring{left:784px;top:72px;width:332px;height:332px;border-radius:50%;border:2px solid rgba(255,255,255,.85)}
.diff-photo{left:792px;top:80px;width:316px;height:316px;border-radius:50%;background:linear-gradient(135deg,#f2ece2,#c7b9a4 50%,#6b7aa6)}

/* solutions */
.solutions{top:2297px;height:466px}
.solutions .heading{top:75px;width:1200px}
.service{top:198px;width:170px;text-align:center}
.service svg{display:block;margin:0 auto}
.service p{margin-top:10px;font-size:14px;line-height:21px;color:#222}

/* check-up */
.checkup{top:2763px;height:420px;background:var(--pale)}
.calc-photo{left:250px;top:75px;width:250px;height:300px;border-radius:18px;background:linear-gradient(160deg,#ffffff,#e4e7ec 55%,#c9ced8);transform:rotate(-22deg);box-shadow:0 18px 30px rgba(20,30,70,.18)}
.checkup h2{left:592px;top:85px;font-family:"Merriweather",serif;font-weight:700;font-size:28px;line-height:37.5px;color:var(--ink)}
.checkup h2 .accent{color:var(--royal)}
.checkup .copy{left:592px;top:176px;width:420px;font-size:11.5px;line-height:21px}
.checkup .btn{left:590px;top:298px;width:418px;height:39px}

/* footer */
.footer{top:3140px;height:434px}
.footer-wave{left:0;top:0}
.footer .brand{left:61px;top:138px}
.footer .about{left:61px;top:198px;width:450px;font-size:11.5px;line-height:21px;color:#e2e6f6}
.footer h4{font-family:"Merriweather",serif;font-weight:700;font-size:16px;color:var(--white)}
.footer .contact-title{left:563px;top:158px}
.footer .links-title{left:838px;top:158px}
.contact-row{left:563px;display:flex;gap:18px;align-items:flex-start;color:var(--white);font-size:12px;line-height:19px}
.contact-row .ico{width:32px;height:32px;border-radius:50%;background:#3a4aa8;display:flex;align-items:center;justify-content:center;flex:none}
.quick{left:838px;top:196px;list-style:none}
.quick li{font-size:11.5px;color:#dfe3f5;margin-bottom:9px;display:flex;align-items:center;gap:14px}
.quick li::before{content:"";width:5px;height:5px;border-radius:50%;background:#4b5bc0}
.footer .rule{left:61px;top:384px;width:1078px;height:1px;background:rgba(255,255,255,.12)}
.footer .legal{top:405px;width:1200px;text-align:center;font-size:11px;color:#cfd5ee}
.footer .legal span{color:#6f7ee0}
</style>
</head>
<body>

<div class="topbar abs" style="position:absolute;left:0;width:1200px">
  <div class="phone abs">
    <svg width="15" height="15" viewBox="0 0 24 24" fill="#fff"><path d="M6.6 10.8a15.1 15.1 0 0 0 6.6 6.6l2.2-2.2c.3-.3.7-.4 1-.2 1.1.4 2.3.6 3.6.6.6 0 1 .4 1 1V20c0 .6-.4 1-1 1A17 17 0 0 1 3 4c0-.6.4-1 1-1h3.5c.6 0 1 .4 1 1 0 1.3.2 2.5.6 3.6.1.3 0 .7-.2 1z"/></svg>
    123 456 7890
  </div>
  <div class="start abs">Start Convertions</div>
</div>

<header class="site-header">
  <div class="brand abs"><span class="mark"></span><span class="name">MERIDALE</span></div>
  <nav class="nav abs">
    <a style="left:4px">Home<span class="caret"></span></a>
    <a style="left:60px">About Us</a>
    <a style="left:132px">Strategies</a>
    <a style="left:208px">Solutions</a>
    <a style="left:278px">Contact Us</a>
  </nav>
  <div class="badge abs" role="img" aria-label="Accredited Wealth Steward badge"><span class="box"></span><span class="lines"><span></span><span></span><span></span></span></div>
</header>

<section class="hero">
  <div class="hero-photo abs" role="img" aria-label="Photo of a financial advisor working at a desk with a monitor, laptop and calculator"></div>
  <svg class="hero-wave abs" width="1200" height="614" viewBox="0 0 1200 614">
    <defs>
      <linearGradient id="heroBand" x1="0" x2="1" y1="0" y2="0">
        <stop offset="0" stop-color="#27328f"/><stop offset=".55" stop-color="#5a67c0"/><stop offset="1" stop-color="#c2cbeb"/>
      </linearGradient>
    </defs>
    <path d="M0 368 C150 520 420 560 640 540 C860 520 1040 500 1200 520 L1200 614 L0 614 Z" fill="url(#heroBand)"/>
    <path d="M0 410 C150 560 420 600 660 580 C880 560 1060 580 1200 620 L1200 614 L0 614 Z" fill="#fff"/>
  </svg>
  <h1 class="abs">Find Your Path To<br>A <span class="accent">Brighter</span><br>Financial Future</h1>
  <p class="tag abs">Wealth Management Firm</p>
  <a class="btn btn-orange">Contact Us Today</a>
</section>

<section class="tax">
  <h2 class="heading abs">The Most Effective Financial Plans<br><span class="accent">Start With Tax Planning.</span></h2>
  <p class="copy abs">Few financial advisors offer tax expertise, but when they do, you benefit.&nbsp; Learn how our unique team combines financial planning, investments and smart tax and income generation strategies to help you achieve your goals faster.</p>
  <a class="btn btn-blue">Learn Why We’re Different</a>
</section>

<section class="strategies">
  <h2 class="heading abs">Better Strategies To Preserve And Grow Wealth,<br><span class="accent">Generate Income and Reduce Your Taxes</span></h2>
  <p class="sub abs">Here’s what you can expect when you work with Meridale.</p>
  <div class="card-photo p1 abs" role="img" aria-label="Photo of a businessman silhouetted inside a glowing light bulb"></div>
  <div class="card-photo p2 abs" role="img" aria-label="Photo of a hand stacking blocks rated with stars"></div>
  <div class="card-photo p3 abs" role="img" aria-label="Photo of an advisor reviewing charts with a calculator"></div>
  <article class="card c1 abs"><h3>A Better Approach</h3><p>Taxes are critical to every financial move you make, so we incorporate tax planning in everything we do for you. Along with managing your investments.</p><a>Explore More</a></article>
  <article class="card c2 abs"><h3>More Experience</h3><p>You’ve worked hard to get where you are, so your money shouldn’t have to be part of any one’s learning curve. At Meridale Asset Advisors, you’ll only work with seasoned</p><a>Explore More</a></article>
  <article class="card c3 abs"><h3>On Your Side</h3><p>In an industry rife with conflicts of interest, you need a firm that works in your best interest. As an independent firm, we have no ties to insurance or mutual</p><a>Explore More</a></article>
</section>

<section class="difference">
  <h2 class="abs">Cookie-Cutter Financial<br>Planning And Investment Can<br><span class="accent">Leave Your Future At Risk.<br>That’s Why We Do It<br>Differently</span></h2>
  <p class="copy abs">Few financial advisors offer tax expertise, but when they do, you benefit. Learn how our unique team combines financial planning, investments and smart tax and income generation strategies to help you achieve your goals faster.</p>
  <a class="btn btn-blue">Meet Our Specialists</a>
  <div class="diff-art abs" role="img" aria-label="Blue panel with sweeping decorative curves"></div>
  <div class="diff-ring abs"></div>
  <div class="diff-photo abs" role="img" aria-label="Photo of an advisor meeting a senior couple at home"></div>
</section>

<section class="solutions">
  <h2 class="heading abs">Personalized Solutions To<br><span class="accent">Help Your Money Work Harder For You</span></h2>
  <div class="service abs" style="left:137px">
    <svg width="140" height="112" viewBox="0 0 140 112"><path d="M18 58 A52 52 0 0 1 122 58" fill="none" stroke="#2e3a96" stroke-width="2"/><circle cx="70" cy="58" r="48" fill="#e6edf8"/><g fill="none" stroke="#1b1f4b" stroke-width="2"><rect x="56" y="40" width="22" height="30" rx="2"/><path d="M60 50h14M60 56h10"/><circle cx="80" cy="66" r="9"/></g></svg>
    <p>Investment<br>Management</p>
  </div>
  <div class="service abs" style="left:327px">
    <svg width="140" height="112" viewBox="0 0 140 112"><path d="M18 58 A52 52 0 0 1 122 58" fill="none" stroke="#2e3a96" stroke-width="2"/><circle cx="70" cy="58" r="48" fill="#e6edf8"/><g fill="none" stroke="#1b1f4b" stroke-width="2"><rect x="57" y="40" width="26" height="34" rx="2"/><rect x="61" y="44" width="18" height="7"/><path d="M61 57h4M68 57h4M75 57h4M61 63h4M68 63h4M75 63h4M61 69h4M68 69h4M75 69h4"/></g></svg>
    <p>Comprehensive<br>Financial Planning</p>
  </div>
  <div class="service abs" style="left:515px">
    <svg width="140" height="112" viewBox="0 0 140 112"><path d="M18 58 A52 52 0 0 1 122 58" fill="none" stroke="#2e3a96" stroke-width="2"/><circle cx="70" cy="58" r="48" fill="#e6edf8"/><g fill="none" stroke="#1b1f4b" stroke-width="2"><path d="M60 40v24h22M64 64v8M78 64v8M56 74c8 4 22 4 30 0"/><circle cx="70" cy="36" r="6"/></g></svg>
    <p>Retirement Income<br>Planning</p>
  </div>
  <div class="service abs" style="left:703px">
    <svg width="140" height="112" viewBox="0 0 140 112"><path d="M18 58 A52 52 0 0 1 122 58" fill="none" stroke="#2e3a96" stroke-width="2"/><circle cx="70" cy="58" r="48" fill="#e6edf8"/><g fill="none" stroke="#1b1f4b" stroke-width="2"><path d="M58 38h20v36H58z"/><circle cx="68" cy="48" r="6"/><path d="M62 62h12M62 68h8"/><circle cx="82" cy="70" r="6"/></g></svg>
    <p>Tax<br>Planning</p>
  </div>
  <div class="service abs" style="left:890px">
    <svg width="140" height="112" viewBox="0 0 140 112"><path d="M18 58 A52 52 0 0 1 122 58" fill="none" stroke="#2e3a96" stroke-width="2"/><circle cx="70" cy="58" r="48" fill="#e6edf8"/><g fill="none" stroke="#1b1f4b" stroke-width="2"><path d="M56 48l14-9 14 9M58 48v24h24V48M63 54h4v5h-4zM73 54h4v5h-4zM67 64h6v8h-6z"/></g></svg>
    <p>Estate<br>Planning</p>
  </div>
</section>

<section class="checkup">
  <div class="calc-photo abs" role="img" aria-label="Photo of a white calculator tilted at an angle"></div>
  <h2 class="abs">The Meridale $549<br><span class="accent">Retirement Check-Up</span></h2>
  <p class="copy abs">We know it’s a big decision to hire or switch advisors. That’s why we provide an easy way to try us out.&nbsp; At the same time, you can get a valuable second opinion to find out if you’re on track to retire. There’s no pressure, and either way, you’ll walk away with valuable insights on what you should be doing to secure your future.</p>
  <a class="btn btn-blue">Learn More About The $549 Retirement Checkup</a>
</section>

<footer class="footer">
  <svg class="footer-wave abs" width="1200" height="434" viewBox="0 0 1200 434">
    <defs>
      <linearGradient id="footBand" x1="0" x2="1"><stop offset="0" stop-color="#2a3590"/><stop offset="1" stop-color="#6a78c8"/></linearGradient>
    </defs>
    <path d="M0 10 C260 50 520 110 760 80 C950 55 1100 20 1200 0 L1200 434 L0 434 Z" fill="url(#footBand)"/>
    <path d="M0 50 C260 90 520 150 780 115 C960 90 1100 70 1200 60 L1200 434 L0 434 Z" fill="#1b2062"/>
    <path d="M0 90 C300 130 600 170 1200 120 L1200 434 L0 434 Z" fill="#1b1f4b"/>
  </svg>
  <div class="brand abs"><span class="mark"></span><span class="name">MERIDALE</span></div>
  <p class="about abs">With over 55 years of combined experience, Meridale Asset Advisors helps successful people more effectively prepare for the future.&nbsp; Our unique small team of wealth managers, financial planners and tax professionals bring you the strategies you need to preserve your wealth, minimize your taxes and create a confident retirement. While we’re based in Ashmere County, Ohio, we serve clients nationwide.</p>

  <h4 class="contact-title abs">Contact Us</h4>
  <div class="contact-row abs" style="top:196px">
    <span class="ico"><svg width="14" height="16" viewBox="0 0 24 24" fill="#fff"><path d="M12 2a7 7 0 0 0-7 7c0 5 7 13 7 13s7-8 7-13a7 7 0 0 0-7-7zm0 9.5A2.5 2.5 0 1 1 12 6.5a2.5 2.5 0 0 1 0 5z"/></svg></span>
    <span>MERIDALE ASSET ADVISORS<br>101 – Lorem ipsum simple text<br>print type industry.</span>
  </div>
  <div class="contact-row abs" style="top:264px;align-items:center">
    <span class="ico"><svg width="14" height="14" viewBox="0 0 24 24" fill="#fff"><path d="M6.6 10.8a15.1 15.1 0 0 0 6.6 6.6l2.2-2.2c.3-.3.7-.4 1-.2 1.1.4 2.3.6 3.6.6.6 0 1 .4 1 1V20c0 .6-.4 1-1 1A17 17 0 0 1 3 4c0-.6.4-1 1-1h3.5c.6 0 1 .4 1 1 0 1.3.2 2.5.6 3.6.1.3 0 .7-.2 1z"/></svg></span>
    <span style="font-size:14px">123 456 7890</span>
  </div>
  <div class="contact-row abs" style="top:308px;align-items:center">
    <span class="ico"><svg width="14" height="12" viewBox="0 0 24 20" fill="#fff"><path d="M2 2h20v16H2z" fill="none"/><path d="M2 2h20l-10 8z"/><path d="M2 5l10 8 10-8v13H2z"/></svg></span>
    <span style="font-size:13px">info@meridale.example</span>
  </div>

  <h4 class="links-title abs">Quick Links</h4>
  <ul class="quick abs"><li>About Us</li><li>Contact Us</li><li>Privacy Policy</li><li>Disclosures</li></ul>

  <div class="rule abs"></div>
  <p class="legal abs">©<span>Meridale Asset Advisors</span> – 2021 All rights reserved.</p>
</footer>

</body>
</html>
```